Grand Opening for Brightvale Church

Would like to have a BillBoard Created according to the specs listed by the company who will be producing the print. I am attaching the spec sheet to this post. I am also attaching a couple different picture options as well as a former Billboard design that was done. I would like the design to incorporate my logo, picture. I am okay if the background on the picture is eliminated for creative purposes. The words to be displayed is "Grand Opening" April 12, 2020 at the former Harlan Middle School) 41st Copper Lake Rd.

Colors

Designer to choose colors to be used in the design.

Requirements
Must have
• Something that pops
Nice to have
• Good color coordinations and clearly visible text

```html
<!DOCTYPE html>
<html lang="en">
<head>
<meta charset="utf-8">
<title>Brightvale Church – Grand Opening Billboard</title>
<link rel="stylesheet" href="https://fonts.googleapis.com/css2?family=Oswald:wght@700&family=Montserrat:wght@500;600&display=swap">
<style>
  :root {
    --page-bg: #c4c4c4;
    --board-dark: #1a0707;
    --board-mid: #2a0f0c;
    --accent-orange: #f39a35;
    --accent-red: #e43d3a;
    --title-top: #e8321f;
    --title-bottom: #f7a12c;
    --ink-dark: #1a0a06;
    --ink-light: #ffffff;
    --photo-warm: #8a4a22;
  }
  * { margin: 0; padding: 0; box-sizing: border-box; }
  html, body {
    width: 1200px; height: 1200px; overflow: hidden;
    background: var(--page-bg);
  }
  .billboard {
    position: absolute; left: 40px; top: 332px;
    width: 1120px; height: 536px; overflow: hidden;
    background: linear-gradient(90deg, var(--board-dark) 0%, var(--board-mid) 55%, var(--board-dark) 100%);
  }
  .speaker-photo {
    position: absolute; left: 545px; top: 0; width: 575px; height: 536px;
    background:
      radial-gradient(ellipse 55% 60% at 62% 78%, var(--photo-warm) 0%, rgba(138,74,34,0.55) 45%, rgba(58,22,12,0) 80%),
      radial-gradient(ellipse 30% 28% at 60% 30%, rgba(110,60,35,0.7) 0%, rgba(58,22,12,0) 75%);
  }
  .headline-frame {
    position: absolute; left: 59px; top: 53px; width: 598px; height: 265px;
    border: 3px solid var(--accent-orange);
  }
  .headline-title {
    position: absolute; left: 0; right: 0; top: 14px;
    display: flex; justify-content: center;
    white-space: nowrap;
    font-family: "Oswald", sans-serif; font-weight: 700; font-size: 88px;
    line-height: 1; letter-spacing: -1px;
    transform: scaleY(1.18); transform-origin: center top;
  }
  .headline-title span {
    background: linear-gradient(180deg, var(--title-top) 15%, var(--title-bottom) 90%);
    -webkit-background-clip: text; background-clip: text; color: transparent;
    -webkit-text-stroke: 1px rgba(255,255,255,0.85);
  }
  .headline-date {
    position: absolute; left: 0; right: 0; top: 127px; text-align: center;
    white-space: nowrap;
    font-family: "Montserrat", sans-serif; font-weight: 600; font-size: 50px;
    line-height: 1; color: var(--accent-orange);
  }
  .location-band {
    position: absolute; left: 0; bottom: 0; width: 592px; height: 69px;
  }
  .location-band svg { position: absolute; inset: 0; }
  .location-venue, .location-road {
    position: absolute; top: 0; height: 69px;
    display: flex; align-items: center; justify-content: center; text-align: center;
    font-family: "Montserrat", sans-serif; font-weight: 600; font-size: 22px; line-height: 1.1;
  }
  .location-venue { left: 0; width: 300px; color: var(--ink-dark); }
  .location-road { left: 305px; width: 287px; color: var(--ink-light); }
  .church-name {
    position: absolute; left: 225px; top: 410px;
    display: flex; align-items: center; gap: 12px;
    font-family: "Montserrat", sans-serif; font-weight: 500; font-size: 34px;
    color: var(--accent-orange); white-space: nowrap;
  }
  .church-name .mark {
    width: 18px; height: 18px; border-radius: 50%; background: var(--accent-orange);
  }
</style>
</head>
<body>
  <div class="billboard">
    <div class="speaker-photo" role="img" aria-label="Photo of the pastor speaking with open hands, wearing a brown jacket"></div>

    <div class="headline-frame">
      <div class="headline-title"><span>GRAND OPENING</span></div>
      <div class="headline-date">APRIL 12, 2020</div>
      <div class="location-band">
        <svg width="592" height="69" viewBox="0 0 592 69" aria-hidden="true">
          <rect x="0" y="0" width="592" height="69" fill="var(--accent-red)"/>
          <polygon points="0,0 280,0 320,34.5 280,69 0,69" fill="var(--accent-orange)"/>
        </svg>
        <div class="location-venue">HARLAN MIDDLE<br>SCHOOL</div>
        <div class="location-road">41ST COPPER LAKE<br>ROAD</div>
      </div>
    </div>

    <div class="church-name"><span class="mark"></span>Brightvale Church</div>
  </div>
</body>
</html>
```